Business cards Marta Kessel Sport & Events

I need new business cards to match my new logo design for my company called "Marta Kessel Sport & Events". I'm based in Germany.
With my company, I offer different services in the context of sport.

Marta Kessel owner

Marta Kessel Sports & Events
Birkenfelder Weg 12
D-63118 Offenbach

+49 69 / 31 52 94 07
info@marta-kessel.example
www.marta-kessel.example

Contact Information for Business Card

Marta Kessel Inhaberin Marta Kessel Sport & Events Birkenfelder Weg 12 D-63118 Offenbach +49 69 / 31 52 94 07 info@marta-kessel.example www.marta-kessel.example

Requirements
Must have
• Logo | Double sided business card

```html
<!DOCTYPE html>
<html lang="de">
<head>
<meta charset="utf-8">
<title>Marta Kessel Sport &amp; Events – Visitenkarten</title>
<link rel="stylesheet" href="https://fonts.googleapis.com/css2?family=Inter:wght@400;500;600;700&display=swap">
<style>
  :root {
    --stage: #e6e6e8;
    --card-dark: #161616;
    --mark-dark: #2c2c2c;
    --card-light: #ffffff;
    --accent: #f5a21b;
    --ink: #141414;
  }
  * { box-sizing: border-box; margin: 0; padding: 0; }
  html, body { width: 1200px; height: 800px; overflow: hidden; }
  body {
    background: var(--stage);
    font-family: "Inter", sans-serif;
    color: var(--ink);
    position: relative;
  }
  .card {
    position: absolute;
    top: 225px;
    width: 540px;
    height: 349px;
  }
  .card--front { left: 40px; background: var(--card-dark); }
  .card--back { left: 620px; background: var(--card-light); }

  /* front */
  .front-mark {
    position: absolute;
    left: 212px; top: 72px;
    width: 116px; height: 116px;
    border: 9px solid var(--mark-dark);
    border-radius: 50%;
  }
  .front-name {
    position: absolute;
    left: 0; right: 0; top: 206px;
    text-align: center;
    font-weight: 700;
    font-size: 26px;
    letter-spacing: 2px;
    line-height: 1.15;
    color: var(--mark-dark);
    text-transform: uppercase;
  }

  /* back */
  .brand {
    position: absolute;
    left: 30px; top: 36px;
    display: flex; align-items: center; gap: 10px;
  }
  .brand-circle {
    width: 86px; height: 86px;
    border: 8px solid var(--accent);
    border-radius: 50%;
  }
  .brand-name {
    font-weight: 700;
    font-size: 19px;
    letter-spacing: 1.5px;
    line-height: 1.2;
    text-transform: uppercase;
    color: var(--ink);
  }
  .person {
    position: absolute;
    left: 27px; top: 196px;
    font-weight: 600;
    font-size: 22px;
    color: var(--accent);
  }
  .role {
    position: absolute;
    left: 27px; top: 225px;
    font-size: 13px;
    letter-spacing: 0.5px;
  }
  .rule {
    position: absolute;
    left: 95px; right: 0; top: 235px;
    height: 1px;
    background: var(--accent);
  }
  .contacts {
    position: absolute;
    left: 27px; top: 256px;
    list-style: none;
    font-size: 13.5px;
    letter-spacing: 0.4px;
  }
  .contacts li {
    display: flex; align-items: center; gap: 5px;
    height: 22.5px;
  }
  .contacts svg { width: 13px; height: 13px; flex: none; }
  .address {
    position: absolute;
    right: 31px; top: 278px;
    text-align: right;
    font-style: normal;
    font-size: 13.5px;
    line-height: 22.5px;
  }
</style>
</head>
<body>
  <section class="card card--front" aria-label="Vorderseite">
    <div class="front-mark"></div>
    <p class="front-name">Marta Kessel<br>Sport &amp; Events</p>
  </section>

  <section class="card card--back" aria-label="Rückseite">
    <div class="brand">
      <div class="brand-circle"></div>
      <p class="brand-name">Marta Kessel<br>Sport &amp; Events</p>
    </div>

    <h1 class="person">MARTA KESSEL</h1>
    <p class="role">Inhaberin</p>
    <div class="rule"></div>

    <ul class="contacts">
      <li>
        <svg viewBox="0 0 16 16" aria-hidden="true"><circle cx="8" cy="8" r="8" fill="#f5a21b"/><path d="M5.2 4.3l1.3-.3.8 1.8-.9.7c.4.9 1.1 1.6 2 2l.7-.9 1.8.8-.3 1.3c-3 .3-5.6-2.4-5.4-5.4z" fill="#fff"/></svg>
        +49 69 / 31 52 94 07
      </li>
      <li>
        <svg viewBox="0 0 16 16" aria-hidden="true"><circle cx="8" cy="8" r="8" fill="#f5a21b"/><rect x="4.3" y="5.3" width="7.4" height="5.4" rx=".6" fill="#fff"/><path d="M4.6 5.7L8 8.3l3.4-2.6" fill="none" stroke="#f5a21b" stroke-width=".9"/></svg>
        info@marta-kessel.example
      </li>
      <li>
        <svg viewBox="0 0 16 16" aria-hidden="true"><circle cx="8" cy="8" r="8" fill="#f5a21b"/><circle cx="8" cy="8" r="3.8" fill="none" stroke="#fff" stroke-width="1"/><path d="M4.2 8h7.6M8 4.2c-1.6 2.2-1.6 5.4 0 7.6M8 4.2c1.6 2.2 1.6 5.4 0 7.6" fill="none" stroke="#fff" stroke-width=".8"/></svg>
        www.marta-kessel.example
      </li>
    </ul>

    <address class="address">
      Birkenfelder Weg 12<br>
      63118 Offenbach Germany
    </address>
  </section>
</body>
</html>
```